Logo for Internal Medicine practice

I want a logo for my Internal Medicine practice, I would like it to be with my name on it which is Lucía Barrenechea Ruiz.

I would like the business card to say the following (it is in Spanish since my practice is in Spanish):

Lucía Barrenechea Ruiz
Medicina Interna
Cel. 5583617204
luciabarrenechearuiz@correovela.mx

Logo Text

Lucía Barrenechea

```html
<!DOCTYPE html>
<html lang="es">
<head>
<meta charset="utf-8">
<title>Lucía Barrenechea Ruiz · Tarjeta de presentación</title>
<link rel="stylesheet" href="https://fonts.googleapis.com/css2?family=Montserrat:wght@700&family=Arimo:wght@400&display=swap">
<style>
  :root {
    --brand-blue: #1b78d3;
    --brand-blue-soft: #3089df;
    --brand-green: #6ea843;
    --card-white: #ffffff;
    --ink: #1a1a1a;
    --backdrop: #2a2a2a;
  }
  * { box-sizing: border-box; margin: 0; padding: 0; }
  html, body {
    width: 1200px; height: 1015px; overflow: hidden;
    background: var(--backdrop);
  }
  .stage {
    width: 1200px; height: 1015px;
    display: flex; flex-direction: column; align-items: center; justify-content: center;
    gap: 48px;
  }
  .card {
    width: 760px; height: 434px; position: relative; overflow: hidden;
  }

  /* Back */
  .card--back {
    background: var(--brand-blue);
    display: flex; align-items: center; justify-content: center; gap: 26px;
  }
  .back-mark__circle {
    width: 70px; height: 70px; border-radius: 50%;
    background: var(--brand-blue-soft); flex: none;
  }
  .back-mark__name {
    font-family: "Montserrat", sans-serif; font-weight: 700; font-size: 56px;
    color: var(--brand-blue-soft); white-space: nowrap;
  }

  /* Front */
  .card--front { background: var(--card-white); }

  .brand {
    position: absolute; top: 48px; left: 0; right: 0; height: 110px;
    display: flex; align-items: center; justify-content: center; gap: 20px;
  }
  .brand__circle {
    width: 52px; height: 52px; border-radius: 50%; background: var(--brand-green); flex: none;
  }
  .brand__name {
    font-family: "Montserrat", sans-serif; font-weight: 700; font-size: 46px;
    color: var(--brand-blue); white-space: nowrap;
  }

  .name-band {
    position: absolute; top: 192px; left: 0; width: 100%; height: 116px;
    background: var(--brand-blue); color: var(--card-white);
    display: flex; flex-direction: column; align-items: center; justify-content: center;
  }
  .name-band__name {
    font-family: "Montserrat", sans-serif; font-weight: 700; font-size: 36px; white-space: nowrap;
  }
  .name-band__role {
    font-family: "Arimo", sans-serif; font-size: 24px; margin-top: 4px;
  }

  .contact {
    position: absolute; top: 322px; left: 0; width: 100%;
    display: flex; align-items: center; justify-content: center; gap: 14px;
    font-family: "Arimo", sans-serif; font-size: 23px; color: var(--ink); white-space: nowrap;
  }
  .contact__item { display: flex; align-items: center; gap: 7px; }
  .contact__icon { width: 22px; height: 22px; flex: none; }

  .divider {
    position: absolute; top: 368px; left: 0; width: 100%; height: 12px; display: flex;
  }
  .divider__blue { flex: 0 0 58%; background: var(--brand-blue); }
  .divider__green { flex: 1; background: var(--brand-green); margin-left: 6px; }

  .foot-strip {
    position: absolute; bottom: 0; left: 0; width: 100%; height: 22px; background: var(--brand-blue);
  }
</style>
</head>
<body>
  <main class="stage">
    <section class="card card--back" aria-label="Reverso de la tarjeta">
      <span class="back-mark__circle"></span>
      <span class="back-mark__name">Lucía Barrenechea</span>
    </section>

    <section class="card card--front" aria-label="Anverso de la tarjeta">
      <div class="brand">
        <span class="brand__circle"></span>
        <span class="brand__name">Lucía Barrenechea</span>
      </div>

      <div class="name-band">
        <p class="name-band__name">Lucía Barrenechea Ruiz</p>
        <p class="name-band__role">Medicina Interna</p>
      </div>

      <div class="contact">
        <span class="contact__item">
          <svg class="contact__icon" viewBox="0 0 24 24" aria-hidden="true">
            <path fill="#1b78d3" d="M6.6 10.8a15.1 15.1 0 0 0 6.6 6.6l2.2-2.2a1 1 0 0 1 1-.25 11.4 11.4 0 0 0 3.6.57 1 1 0 0 1 1 1V20a1 1 0 0 1-1 1A17 17 0 0 1 3 4a1 1 0 0 1 1-1h3.5a1 1 0 0 1 1 1c0 1.25.2 2.45.57 3.57a1 1 0 0 1-.25 1z"/>
          </svg>
          5583617204
        </span>
        <span class="contact__item">
          <svg class="contact__icon" viewBox="0 0 24 24" aria-hidden="true">
            <rect x="2" y="5" width="20" height="14" fill="#1b78d3"/>
            <path d="M2 5l10 8 10-8M2 19l7-7M22 19l-7-7" fill="none" stroke="#fff" stroke-width="1.5"/>
          </svg>
          luciabarrenechearuiz@correovela.mx
        </span>
      </div>

      <div class="divider">
        <span class="divider__blue"></span>
        <span class="divider__green"></span>
      </div>

      <div class="foot-strip"></div>
    </section>
  </main>
</body>
</html>
```